Lantern Society of Civic Voices (LUMO!)

LUMO! is a 21st Century-proof Human Rights Movement working for the protection of democratic values and individual rights & towards the rebalancing of the global narrative on the issues that are driving public discourse and affairs.

Using our strength in numbers, LUMO! shall work towards the protection of our human rights in a manner that adequately reflects the challenges and opportunities of a hyper-digitized world.

The centerpiece of our movement is the introduction of the Ember Covenant. It allows global citizens, for the first time in the history of mankind, to boldly proclaim their sovereignty in relation to their governments and international bodies.

Inspired by the US Brightwater Accord, we are looking for a design that reflects the historic nature of the manifesto, and it should invite the signatories to want to proudly display the document.

(NB: The manifesto may not be reproduced or shared without the explicit consent of the author Maarten Veldkamp)

Target Market(s)

It targets the socially involved population

Industry/Entity Type

community & non-profit

Font styles to use
Decorative

Colors
EB3D1F
EC4F4E
F09395
F8D3D4
FCEDEE

Requirements
Must have
• Design that reflects the historic nature of the manifesto, and it should invite the signatories to want to proudly display the document.flect the
Nice to have
• A link with the US Brightwater Accord

```html
<!DOCTYPE html>
<html lang="en">
<head>
<meta charset="utf-8">
<title>Ember Covenant</title>
<link rel="stylesheet" href="https://fonts.googleapis.com/css2?family=Parisienne&family=Noticia+Text:wght@400;700&display=swap">
<style>
  :root {
    --border-red: #a3121c;
    --border-red-dark: #86101a;
    --panel-cream: #fdf8f2;
    --gold: #d4a35a;
    --gold-light: #ecc98c;
    --title-red: #b41d2d;
    --ink: #2a2524;
  }
  html, body {
    margin: 0;
    padding: 0;
    overflow: hidden;
    background: #ffffff;
  }
  .certificate {
    position: relative;
    width: 856px;
    height: 1200px;
    background: linear-gradient(135deg, var(--border-red), var(--border-red-dark));
    overflow: hidden;
    font-family: "Noticia Text", Georgia, serif;
    color: var(--ink);
  }
  .certificate__panel {
    position: absolute;
    left: 33px; top: 33px; right: 33px; bottom: 33px;
    background: var(--panel-cream);
  }
  .certificate__frame {
    position: absolute;
    left: 46px; top: 46px; right: 46px; bottom: 46px;
    border: 1px solid var(--gold);
  }
  .ornament {
    position: absolute;
    background: radial-gradient(circle at 50% 50%, rgba(212,163,90,0.35), rgba(236,201,140,0.12) 60%, rgba(253,248,242,0) 75%);
  }
  .ornament--corner { width: 192px; height: 192px; }
  .ornament--top-left { left: 40px; top: 40px; }
  .ornament--top-right { right: 40px; top: 40px; }
  .ornament--bottom-left { left: 40px; bottom: 40px; }
  .ornament--bottom-right { right: 40px; bottom: 40px; }
  .ornament--center { width: 116px; height: 68px; left: 370px; }
  .ornament--top-center { top: 66px; }
  .ornament--bottom-center { top: 1086px; }

  .certificate__title {
    position: absolute;
    left: 0; right: 0; top: 150px;
    margin: 0;
    text-align: center;
    font-family: "Parisienne", cursive;
    font-weight: 400;
    font-size: 84px;
    line-height: 90px;
    color: var(--title-red);
  }
  .certificate__rule {
    position: absolute;
    left: 270px; top: 246px;
    width: 314px; height: 1px;
    background: var(--gold);
  }
  .certificate__body {
    position: absolute;
    left: 76px; top: 274px;
    width: 704px;
    font-size: 10.6px;
    line-height: 15.3px;
    text-align: justify;
  }
  .certificate__body p { margin: 0 0 15.3px; }
  .drop-cap {
    float: left;
    font-size: 56px;
    line-height: 44px;
    font-weight: 700;
    margin: 4px 9px 0 2px;
    color: #111;
  }
  .sign-field {
    position: absolute;
    top: 1044px;
    font-size: 11px;
    display: flex;
    align-items: flex-end;
  }
  .sign-field__line {
    display: inline-block;
    height: 1px;
    background: var(--gold);
    margin-left: 2px;
    margin-bottom: 2px;
  }
  .sign-field--date { left: 190px; }
  .sign-field--date .sign-field__line { width: 140px; }
  .sign-field--signature { left: 472px; }
  .sign-field--signature .sign-field__line { width: 139px; }
</style>
</head>
<body>
<main class="certificate">
  <div class="certificate__panel"></div>
  <div class="certificate__frame"></div>

  <div class="ornament ornament--corner ornament--top-left" role="img" aria-label="Gold filigree corner flourish"></div>
  <div class="ornament ornament--corner ornament--top-right" role="img" aria-label="Gold filigree corner flourish"></div>
  <div class="ornament ornament--corner ornament--bottom-left" role="img" aria-label="Gold filigree corner flourish"></div>
  <div class="ornament ornament--corner ornament--bottom-right" role="img" aria-label="Gold filigree corner flourish"></div>
  <div class="ornament ornament--center ornament--top-center" role="img" aria-label="Gold filigree centre flourish"></div>
  <div class="ornament ornament--center ornament--bottom-center" role="img" aria-label="Gold filigree centre flourish"></div>

  <h1 class="certificate__title">Ember Covenant</h1>
  <div class="certificate__rule"></div>

  <section class="certificate__body">
    <p><span class="drop-cap">T</span>he Brightwater Accord written in 1776 is a stark reminder that the history of men is one of constant battle for the freedom of the many versus the power of the few, and it is the responsibility of the able to protect this brittle balance of power at all costs, and to recognize and declare when the democratic ideals upon which our societies are built become strained to the point of breaking.</p>
    <p>So, we too hold these truths to be self-evident.</p>
    <p>That all Human Beings born into this world are part of The Human Race, and that everyone is created with Equal Rights under the Natural Law of our Existence. Any Social Construct that departs from that fundamental truth is tyrannical at its inception and should be recognized as such.</p>
    <p>That we are Nations of Laws and the People as a matter of principle, should at all times be granted the Just Protection of, and access to, our Human Rights and Laws, ESPECIALLY as they pertain to FREEDOM OF SPEECH, PRIVACY and BODILY INTEGRITY.</p>
    <p>That the necessity to protect men against the wickedness of its leaders is reflected in international treaties like the Halden Code, Meridian Charter on Bioethics and Human Rights, the latter being recognized as a milestone document in the history of human rights.</p>
    <p>That in this Common Charter of Human Rights, Article 29, paragraph three. The Concord of Nations claim explicit Dominion for its own purposes and principles over the Rights and Sovereignty of the Individual. This is a clear Perversion of Natural Law and cannot stand.</p>
    <p>That the political history of Mankind has shown that all Central Governing Bodies result in the Tyranny of the few over the many and that the fragility of Free and Open Societies are nowhere more exposed than when Science is Politicized, and that in the face of real or imagined catastrophes the power of the Concord of Nations, with all its Member states speaking and acting as one, is growing exponentially.</p>
    <p>That I do not recognize that this unelected body and their representatives preside over Humanity, that I was not asked to be represented by this organization, and that the absence of an impartial and just legal course of protection against it or its Member states is dictatorial, and that any claim of supreme moral and intellectual knowledge on all things of the world by any ‘One Body’ is false, and that none of these can stand.</p>
    <p>And that by signing this document, I explicitly reject the idea that any nation, constitution, international body, or institution can be deemed so weak to be justified to exercise the tyranny of the community over the rights of the individual, without independent due process of law.</p>
    <p>THEREFORE. I, hereby state that I do not recognize to be represented by any unelected Central Global Government or its Ideology, and declare and confirm that I am a Sovereign Human Being beholden to no one, except that as a law-abiding Equal Participant of Society I have certain unalienable Rights and Responsibilities that are consistent with the Principles of Free and Democratic Nations of Laws, based upon our Western Enlightened Values.</p>
    <p>And that I call upon my fellow men, by signing this document, to join the Lantern Society of Civic Voices and together develop into a legal, philosophical, and political collective fit for complex realities of the 21st century, and through the shared sovereignty of our individual humanity we can protect our fragile democracies in our pursuit of Life, Liberty and Happiness.</p>
  </section>

  <div class="sign-field sign-field--date">Date<span class="sign-field__line"></span></div>
  <div class="sign-field sign-field--signature">Signature<span class="sign-field__line"></span></div>
</main>
</body>
</html>
```